We are Here! Come and Meet the Team Flyer

A clear and quirky, flyer to let local Residents know we have landed.
Based around our logo.

We avoid anything medical but rather focus on being pet-centred, warmth, approachable and community-orientated.

We pride ourselves on being cutting-edge but steer away from a cold sterile image.
Approachability, uptodate. We understandt hat pets are part of a family and we will provide the level of care that we would expect for our own pets.

Target Market(s)

Residents in the area

Industry/Entity Type

Veterinary

Font styles to use
Sans Serif

Colors
33b8a4
ffc214
0255a3

Requirements
Must have
• Logo and PERHAPS a location of Clinic indicated on the cat of the Logo.
• NOW OPEN!
• 1) Exact location of the Clinic indicated: the lefthand side of tail, near the cat's back.
• 2) Warm, quirky, Approachable
• 3) Contact details (see attached draft Poster)
• 4) Location: Silver Brook Arcade, Building 4, Mezzanine level
Should not have
• nothing medical or cliched.

```html
<!DOCTYPE html>
<html lang="en">
<head>
<meta charset="utf-8">
<title>Tail &amp; Whisker – Now in Cedar Bay</title>
<link href="https://fonts.googleapis.com/css2?family=Nunito:wght@700;800;900&family=Raleway:wght@500;600;700&family=Varela+Round&display=swap" rel="stylesheet">
<style>
  :root{
    --backdrop:#c4d4e1;
    --paper:#ffffff;
    --teal-dark:#2f6b80;
    --teal-band:#3a7387;
    --sage:#8fbfa9;
    --orange:#d8892c;
    --orange-light:#eaa336;
    --pattern:#eef2ef;
    --ink:#2b2440;
  }
  *{margin:0;padding:0;box-sizing:border-box}
  html,body{width:1200px;height:1200px;overflow:hidden}
  body{background:var(--backdrop);position:relative;font-family:"Nunito",sans-serif}
  .flyer{position:absolute;left:242px;top:98px;width:716px;height:1005px;background:var(--paper);overflow:hidden}
  .brand-art{position:absolute;left:170px;top:40px;width:225px;height:135px;background:linear-gradient(90deg,#e3a765,#9ccab8);border-radius:8px;opacity:.55}
  .brand-name{position:absolute;left:400px;top:98px;font-family:"Varela Round",sans-serif;font-size:32px;line-height:1;color:var(--orange)}
  .brand-sub{position:absolute;left:400px;top:165px;font-family:"Raleway",sans-serif;font-size:9px;letter-spacing:3.2px;color:var(--ink);font-weight:600}
  .headline-box{position:absolute;left:44px;top:200px;width:629px;height:126px;border:2px solid var(--orange);border-radius:10px}
  .headline{position:absolute;left:0;width:716px;top:205px;text-align:center;font-weight:900;font-size:64px;letter-spacing:1px;color:var(--teal-dark);line-height:1}
  .headline-sub{position:absolute;left:0;width:716px;top:267px;text-align:center;font-family:"Varela Round",sans-serif;font-size:25px;letter-spacing:2.6px;color:var(--sage)}
  .headline-tag{position:absolute;left:188px;width:340px;top:303px;text-align:center;background:var(--paper);font-weight:900;font-size:32px;color:var(--orange);letter-spacing:.5px}
  .pattern-field{position:absolute;left:0;top:345px;width:716px;height:395px;background:var(--pattern)}
  .hero-photo{position:absolute;left:312px;top:370px;width:404px;height:370px;background:linear-gradient(160deg,#d8b68a,#b98a5a 60%,#8e6a48);border-radius:48% 40% 0 0}
  .location-seal{position:absolute;left:39px;top:382px;width:320px;height:320px}
  .location-text{position:absolute;left:95px;top:528px;width:208px;text-align:center;color:#fff;font-weight:800;font-size:17px;line-height:22.5px}
  .location-text small{display:block;font-family:"Raleway",sans-serif;font-weight:500;font-size:12px;line-height:16px}
  .family-photo{position:absolute;left:0;top:740px;width:358px;height:182px;background:linear-gradient(120deg,#3d4a66,#d9d4cc 45%,#8a9ab5 80%,#4a5064)}
  .open-badge{position:absolute;left:54px;top:682px;width:100px;height:100px;border-radius:50%;background:var(--orange);border:4px solid #fff;box-shadow:0 0 0 2px var(--orange);color:#fff;font-weight:900;text-align:center}
  .open-badge .open{display:block;font-size:24px;line-height:1;margin-top:18px}
  .open-badge .days{display:flex;justify-content:center;align-items:center;gap:3px;margin-top:2px}
  .open-badge .num{font-size:32px;line-height:1}
  .open-badge .lbl{font-size:15px;line-height:14px;text-align:left}
  .open-badge .lbl span{font-size:11px;display:block}
  .contact-panel{position:absolute;left:358px;top:740px;width:358px;height:182px;background:linear-gradient(90deg,var(--orange),var(--orange-light))}
  .contact-panel::before{content:"";position:absolute;left:0;top:72px;border-left:14px solid var(--paper);border-top:17px solid transparent;border-bottom:17px solid transparent;opacity:.85}
  .contact-list{position:absolute;left:0;width:358px;top:22px;text-align:center;color:#fff;font-family:"Raleway",sans-serif;font-weight:700;font-size:19px;line-height:25.5px;list-style:none}
  .contact-list .title{font-size:17px;margin-bottom:14px}
  .contact-list svg{width:17px;height:17px;vertical-align:-2px;margin:0 3px}
  .social-band{position:absolute;left:0;top:922px;width:716px;height:83px;background:var(--teal-band);display:flex;justify-content:center;gap:46px;padding-top:18px;color:#fff;font-family:"Raleway",sans-serif;font-weight:500;font-size:17px}
  .social-band span{display:flex;align-items:center;gap:7px}
  .social-band i{width:18px;height:18px;border:2px solid #fff;border-radius:3px;display:inline-block}
</style>
</head>
<body>
<main class="flyer">
  <div class="brand-art" role="img" aria-label="Brand illustration of a dog and a cat with a palm tree"></div>
  <div class="brand-name">tail &amp; whisker</div>
  <div class="brand-sub">VETERINARY CLINIC</div>

  <div class="headline-box"></div>
  <h1 class="headline">DID YOU KNOW?</h1>
  <p class="headline-sub">Cedar Bay now has its own</p>
  <p class="headline-tag">VETERINARY CLINIC</p>

  <div class="pattern-field" role="img" aria-label="Soft repeating pattern of dog and cat silhouettes"></div>
  <div class="hero-photo" role="img" aria-label="Photo of a happy tan dog with its mouth open"></div>

  <svg class="location-seal" viewBox="0 0 320 320" aria-label="Situated in Silver Brook Arcade">
    <defs>
      <path id="arc-top" d="M46,160 A114,114 0 0 1 274,160"/>
      <path id="arc-bottom" d="M18,160 A142,142 0 0 0 302,160"/>
    </defs>
    <circle cx="160" cy="160" r="154" fill="#fff" stroke="#8fbfa9" stroke-width="4"/>
    <circle cx="160" cy="160" r="104" fill="#d8892c"/>
    <text font-family="Nunito, sans-serif" font-weight="900" font-size="40" fill="#2f6b80" letter-spacing="3">
      <textPath href="#arc-top" startOffset="50%" text-anchor="middle">SITUATED IN</textPath>
    </text>
    <text font-family="Nunito, sans-serif" font-weight="900" font-size="34" fill="#2f6b80" letter-spacing="1">
      <textPath href="#arc-bottom" startOffset="50%" text-anchor="middle">SILVERBROOK ARCADE</textPath>
    </text>
  </svg>
  <p class="location-text">Silver Brook Arcade<br>Building 4<br>Mezzanine level<small>(Above Cafe Lumo)</small></p>

  <div class="family-photo" role="img" aria-label="Photo of a girl greeting a small white dog on an exam table"></div>
  <div class="open-badge">
    <span class="open">OPEN</span>
    <span class="days"><span class="num">7</span><span class="lbl">DAYS<span>A WEEK</span></span></span>
  </div>

  <section class="contact-panel">
    <ul class="contact-list">
      <li class="title">How To Contact Us?</li>
      <li>Call <svg viewBox="0 0 20 20"><circle cx="10" cy="10" r="8" fill="none" stroke="#fff" stroke-width="1.8"/><path d="M7 6.5c0 4 2.5 6.5 6.5 6.5l.5-1.8-2-.8-.8.9c-1-.5-1.8-1.3-2.3-2.3l.9-.8-.8-2z" fill="#fff"/></svg> 800-TWV-PETS</li>
      <li>Call <svg viewBox="0 0 20 20"><circle cx="10" cy="10" r="8" fill="none" stroke="#fff" stroke-width="1.8"/><path d="M7 6.5c0 4 2.5 6.5 6.5 6.5l.5-1.8-2-.8-.8.9c-1-.5-1.8-1.3-2.3-2.3l.9-.8-.8-2z" fill="#fff"/></svg> 04 555 0182</li>
      <li>hello@tailwhisker.ae</li>
      <li>www.tailwhisker.ae</li>
    </ul>
  </section>

  <footer class="social-band">
    <span><i></i>@TWVetsCedarBay</span>
    <span><i></i>@tailwhiskervet</span>
    <span><i></i>@twvetclinic</span>
  </footer>
</main>
</body>
</html>
```